Business Card for a Dental Office

The design should communicate integrity, quality and reliability. We also want the card look elegant, simple, but still stand out, different from the traditional-dental-office business card.

Business

```html
<!DOCTYPE html>
<html lang="en">
<head>
<meta charset="utf-8">
<title>Harlow Dental Centre – Business Card</title>
<link rel="stylesheet" href="https://fonts.googleapis.com/css2?family=Bebas+Neue&family=Open+Sans:wght@600&family=Arimo&family=Roboto+Condensed:wght@400&display=swap">
<style>
  :root {
    --yellow: #f1ea1f;
    --yellow-deep: #e2d21f;
    --gold: #c6a52e;
    --gold-text: #b8952a;
    --ink: #231f20;
    --charcoal: #2b2829;
    --white: #ffffff;
  }
  * { margin: 0; padding: 0; box-sizing: border-box; }
  html, body {
    width: 734px; height: 1200px; overflow: hidden; background: var(--white);
  }
  .card {
    position: relative; width: 734px; height: 1200px; overflow: hidden;
  }
  .brand-field {
    position: absolute; left: 0; top: 0; width: 734px; height: 559px;
    background: radial-gradient(ellipse at 35% 60%, var(--yellow) 0%, var(--yellow-deep) 55%, var(--gold) 120%);
    display: flex; align-items: center; justify-content: center; gap: 22px;
  }
  .brand-mark-square {
    width: 64px; height: 64px; background: var(--ink);
  }
  .brand-mark-name {
    font-family: "Bebas Neue", sans-serif; font-size: 150px; line-height: 1;
    color: var(--ink); padding-top: 14px;
  }
  .name-band {
    position: absolute; left: 0; top: 559px; width: 734px; height: 135px;
    background: var(--white);
  }
  .practice-name {
    position: absolute; left: 68px; top: 12px; width: 600px;
    font-family: "Bebas Neue", sans-serif; font-size: 82px; line-height: 1;
    color: var(--ink); letter-spacing: 0.5px; white-space: nowrap;
  }
  .tagline {
    position: absolute; left: 70px; top: 82px; width: 600px;
    font-family: "Open Sans", sans-serif; font-weight: 600; font-size: 27px;
    line-height: 1; letter-spacing: 1.6px; white-space: nowrap;
    color: var(--gold-text);
  }
  .contact-panel {
    position: absolute; left: 0; top: 694px; width: 595px; height: 506px;
    background: var(--charcoal);
  }
  .contact-details {
    position: absolute; left: 74px; top: 40px;
    font-family: "Arimo", sans-serif; font-size: 46px; line-height: 69px;
    color: var(--white); list-style: none; white-space: nowrap;
  }
  .contact-details .spacer { height: 72px; }
  .phone-strip {
    position: absolute; left: 595px; top: 694px; width: 139px; height: 506px;
    background: linear-gradient(90deg, var(--gold) 0%, var(--yellow-deep) 45%, var(--yellow) 100%);
  }
  .phone-strip svg { display: block; }
  .phone-number {
    font-family: "Roboto Condensed", sans-serif; font-size: 86px; fill: var(--ink);
  }
</style>
</head>
<body>
  <main class="card">
    <header class="brand-field">
      <span class="brand-mark-square"></span>
      <span class="brand-mark-name">HARLOW</span>
    </header>

    <section class="name-band">
      <h1 class="practice-name">HARLOW DENTAL CENTRE</h1>
      <p class="tagline">YOUR SMILE IS YOUR GIFT TO OTHERS</p>
    </section>

    <section class="contact-panel">
      <ul class="contact-details">
        <li>Contact Name</li>
        <li class="spacer"></li>
        <li>Contact Number</li>
        <li>Email address</li>
        <li>Address 1, Address 2,</li>
        <li>Address 3</li>
      </ul>
    </section>

    <aside class="phone-strip">
      <svg width="139" height="506" viewBox="0 0 139 506" aria-label="Telephone 01 0987 6543">
        <text class="phone-number" transform="translate(106 441) rotate(-90)"
              textLength="395" lengthAdjust="spacingAndGlyphs">T. 01 0987 6543</text>
      </svg>
    </aside>
  </main>
</body>
</html>
```